CINEMA IN CONCERT

We need a need a flyer that will be used to promote a concert.

The concert name will be "Cinema in Concert", this flyer needs to appeal to all
ages becuase we are playing music from movies such as moon raiders, montana briggs Felix Tumbler and more. I would also like a photo of an orchestra in background so people know there is an actual orchestra playing.

If you use photos from the movies please make sure, I do not have any issues with rights to the photo.

Please make sure to add info into flyer.

"Cinema in Concert"

Location: Brennock Auditorium

Date: September 22nd, 2013 - Sunday

Time: 3:00pm                                   

Target Market(s)

All Audience young and old

Requirements
Must have
• "Cinema in Concert"
• Location: Brennock Auditorium
• Date: September 22nd, 2013 - Sunday
• Time: 3:00pm

```html
<!DOCTYPE html>
<html lang="en">
<head>
<meta charset="utf-8">
<title>Cinema in Concert</title>
<link rel="stylesheet" href="https://fonts.googleapis.com/css2?family=Oswald:wght@500;600&family=Arimo:wght@700&display=swap">
<style>
  :root {
    --frame-light: #ffffff;
    --frame-mid: #9fb6cf;
    --frame-dark: #0b3a78;
    --poster-glow: #2f8be0;
    --poster-core: #1668c4;
    --poster-deep: #0a3f8c;
    --rule: rgba(255, 255, 255, 0.85);
    --ink: #ffffff;
    --art-light: #a9bacd;
    --art-mid: #7088a6;
    --art-dark: #3d5676;
  }
  html, body {
    margin: 0;
    padding: 0;
    overflow: hidden;
  }
  .flyer {
    position: relative;
    width: 829px;
    height: 1200px;
    box-sizing: border-box;
    border: 2px solid #000;
    background: linear-gradient(180deg, var(--frame-light) 0%, var(--frame-light) 22%, var(--frame-mid) 48%, var(--frame-dark) 72%, var(--frame-dark) 100%);
    overflow: hidden;
  }
  .poster {
    position: absolute;
    left: 68px;
    top: 62px;
    width: 688px;
    height: 1068px;
    background: radial-gradient(ellipse 70% 45% at 50% 30%, var(--poster-glow) 0%, var(--poster-core) 55%, var(--poster-deep) 100%);
    overflow: hidden;
  }
  .film-art {
    position: absolute;
    left: 46px;
    top: 62px;
    width: 576px;
    height: 480px;
    border-radius: 18px;
    background: linear-gradient(160deg, var(--art-light) 0%, var(--art-mid) 55%, var(--art-dark) 100%);
    box-shadow: 0 10px 24px rgba(0, 20, 60, 0.35);
  }
  .title {
    position: absolute;
    left: 0;
    width: 100%;
    margin: 0;
    text-align: center;
    color: var(--ink);
    font-family: "Oswald", sans-serif;
    font-weight: 600;
    text-transform: uppercase;
    line-height: 1;
    white-space: nowrap;
    text-shadow: 0 3px 6px rgba(0, 20, 60, 0.35);
  }
  .title-top {
    top: 580px;
    font-size: 78px;
    letter-spacing: 13px;
    text-indent: 13px;
  }
  .title-main {
    top: 649px;
    font-size: 142px;
    letter-spacing: 1px;
    transform: scaleX(0.81);
    transform-origin: 50% 50%;
  }
  .rule {
    position: absolute;
    left: 129px;
    width: 426px;
    height: 2px;
    background: var(--rule);
  }
  .rule-1 { top: 800px; }
  .rule-2 { top: 860px; }
  .rule-3 { top: 956px; }
  .info {
    position: absolute;
    left: 0;
    width: 100%;
    margin: 0;
    text-align: center;
    color: var(--ink);
    font-family: "Arimo", sans-serif;
    font-weight: 700;
    text-transform: uppercase;
    line-height: 1;
    white-space: nowrap;
    text-shadow: 0 2px 4px rgba(0, 20, 60, 0.35);
  }
  .venue {
    top: 815px;
    font-size: 34px;
    letter-spacing: 0.5px;
  }
  .date {
    top: 872px;
    font-size: 75px;
  }
  .date .ordinal {
    font-size: 32px;
    vertical-align: 32px;
    margin-right: 8px;
  }
  .date .month {
    font-size: 44px;
    margin-right: 12px;
  }
  .time {
    top: 982px;
    font-size: 41px;
    letter-spacing: 3.5px;
  }
</style>
</head>
<body>
  <main class="flyer">
    <section class="poster">
      <div class="film-art" role="img" aria-label="Illustration of a film clapperboard with film reels and film canisters"></div>
      <h1 class="title title-top">Cinema in</h1>
      <h1 class="title title-main">Concert</h1>
      <div class="rule rule-1"></div>
      <p class="info venue">Brennock Auditorium</p>
      <div class="rule rule-2"></div>
      <p class="info date">22<span class="ordinal">ND</span><span class="month">Sep.</span>2013</p>
      <div class="rule rule-3"></div>
      <p class="info time">3:00 PM Onwards</p>
    </section>
  </main>
</body>
</html>
```